Redesign of Form/Document Navigation Page

I need a redesign of our document and navigation bar on the left. We want the same navigation bar layout/setup but want the buttons and typography to be simple and matching all over. The form needs to be aesthetically pleasing and fit within the page.

1st attachment is our Direct Deposit and the second is the form continued.

```html
<!DOCTYPE html>
<html lang="en">
<head>
<meta charset="utf-8">
<title>Employee Direct Deposit Enrollment</title>
<link href="https://fonts.googleapis.com/css2?family=Open+Sans:wght@400;600;700&family=Roboto:wght@400&display=swap" rel="stylesheet">
<style>
  :root{
    --brand-blue:#1a5a9e;
    --button-blue:#14528f;
    --gold:#e8a317;
    --page-bg:#ebecef;
    --ink:#333;
    --muted:#555;
    --border:#c9c9c9;
    --footer:#262626;
    --link:#5b3fa8;
  }
  *{box-sizing:border-box;margin:0;padding:0}
  html,body{width:1200px;height:868px;overflow:hidden}
  body{font-family:"Open Sans",sans-serif;background:var(--page-bg);color:var(--ink);position:relative}

  .site-header{position:absolute;left:0;top:0;width:1200px;height:99px;background:#fff}
  .brand{position:absolute;left:92px;top:30px;display:flex;align-items:center;gap:8px}
  .brand-mark{width:36px;height:36px;border-radius:50%;background:var(--brand-blue)}
  .brand-name{font-weight:700;font-size:19px;line-height:20px;color:var(--gold);width:200px}
  .main-nav{position:absolute;left:427px;top:39px;display:flex;gap:30px;font-size:16px;color:#333}
  .user{position:absolute;right:222px;top:40px;font-size:14.5px;display:flex;align-items:center;gap:8px;white-space:nowrap}
  .btn{background:var(--button-blue);color:#fff;font-size:11px;border-radius:2px;display:flex;align-items:center;justify-content:center}
  .back-btn{position:absolute;left:993px;top:35px;width:121px;height:28px}

  .side-nav{position:absolute;left:87px;top:131px;width:273px}
  .side-item{position:absolute;left:0;width:273px;height:83px;background:#fff;border:1px solid var(--border);display:flex;align-items:center;padding-left:20px;gap:14px;font-size:15px;color:var(--brand-blue)}
  .side-item svg{width:36px;height:36px;flex:none}

  .form-panel{position:absolute;left:374px;top:129px;width:740px;height:628px;background:#fff;border:1px solid var(--border);overflow:hidden}
  .scrollbar{position:absolute;right:0;top:0;width:13px;height:100%;background:#f1f1f1}
  .scrollbar span{position:absolute;left:0;top:26px;width:13px;height:89px;background:#a9a9a9}
  .abs{position:absolute;white-space:nowrap}
  .form-title{left:21px;top:30px;font-size:20px;font-weight:400;color:var(--brand-blue)}
  .intro{left:22px;top:67px;width:672px;font-size:10.5px;line-height:17px;color:var(--muted);white-space:normal}
  .note{left:21px;top:126px;font-size:11.5px}
  .attach-box{left:21px;top:154px;width:671px;height:99px;border:1px solid var(--border)}
  .attach-link{position:absolute;left:0;right:0;top:22px;text-align:center;font-size:11px;color:var(--link);text-decoration:underline}
  .refresh{position:absolute;left:297px;top:52px;width:76px;height:28px}
  .section-title{font-size:14.5px;font-weight:400;color:var(--brand-blue)}
  .small{font-size:10.5px;color:var(--muted)}
  .mid{font-size:11.5px}
  .notify{font-size:13px}
  .radio-row{display:flex;gap:22px;font-size:11.5px}
  .radio{display:flex;align-items:center;gap:10px}
  .radio i{width:12px;height:12px;border:1px solid #bbb;border-radius:50%;display:block}
  .field{position:absolute;height:29px;border:1px solid #bdbdbd;font-size:11px;padding-left:11px;display:flex;align-items:center;color:#444}
  .field.select::after{content:"";position:absolute;right:10px;top:12px;border:4px solid transparent;border-top-color:#999}
  .legal{left:20px;top:551px;width:700px;font-size:10.5px;line-height:17px;color:var(--muted);white-space:normal}

  .site-footer{position:absolute;left:0;top:794px;width:1200px;height:74px;background:var(--footer);color:#bbb}
  .copyright{position:absolute;left:86px;top:26px;font-family:"Roboto",sans-serif;font-size:14px}
  .social{position:absolute;left:992px;top:20px;display:flex;gap:5px}
  .social span{width:28px;height:28px;border:1.5px solid #ddd;border-radius:50%}
</style>
</head>
<body>
<header class="site-header">
  <div class="brand"><span class="brand-mark"></span><span class="brand-name">SENTINEL WATCH SERVICES</span></div>
  <nav class="main-nav"><span>HOME</span><span>HELP</span></nav>
  <div class="user">DANA WHITFIELD
    <svg width="17" height="17" viewBox="0 0 18 18" fill="none" stroke="#555" stroke-width="2" stroke-linecap="round"><path d="M5 4.5a6.5 6.5 0 1 0 8 0"/><path d="M9 2v7"/></svg>
  </div>
  <div class="btn back-btn">BACK TO PROFILE</div>
</header>

<nav class="side-nav">
  <div class="side-item" style="top:0">
    <svg viewBox="0 0 36 36"><circle cx="18" cy="18" r="16" fill="var(--brand-blue)"/><text x="18" y="25" text-anchor="middle" font-size="20" font-weight="700" fill="#fff" font-family="Open Sans,sans-serif">$</text></svg>DIRECT DEPOSIT</div>
  <div class="side-item" style="top:89px">
    <svg viewBox="0 0 36 36" fill="none" stroke="var(--brand-blue)" stroke-width="2.5"><rect x="3" y="5" width="30" height="22"/><path d="M9 12h18M9 17h12"/><circle cx="24" cy="26" r="4" fill="var(--brand-blue)"/></svg>CHANGE W-4</div>
  <div class="side-item" style="top:180px">
    <svg viewBox="0 0 36 36" fill="none" stroke="var(--brand-blue)" stroke-width="3.5" stroke-linecap="round"><path d="M6 30L24 12M10 8l6 6M28 30L14 16M26 4l6 6"/></svg>LABOUR CODE</div>
  <div class="side-item" style="top:271px">
    <svg viewBox="0 0 36 36" fill="none" stroke="var(--brand-blue)" stroke-width="2.5"><circle cx="18" cy="18" r="15"/><path d="M18 15v11" stroke-width="3.5"/><circle cx="19" cy="10" r="1.5" fill="var(--brand-blue)"/></svg>PERSONAL INFORMATION</div>
  <div class="side-item" style="top:362px">
    <svg viewBox="0 0 36 36"><rect x="3" y="10" width="30" height="20" fill="var(--brand-blue)"/><rect x="13" y="5" width="10" height="6" fill="none" stroke="var(--brand-blue)" stroke-width="2.5"/><path d="M18 15v10M13 20h10" stroke="#fff" stroke-width="2.5"/></svg>APPRASIAL &amp; REVIEW</div>
  <div class="side-item" style="top:452px">
    <svg viewBox="0 0 36 36" fill="none" stroke="var(--brand-blue)" stroke-width="2.5"><rect x="6" y="3" width="22" height="28"/><path d="M11 10h12M11 15h12M11 20h12M11 25h12M31 8v26H10"/></svg>WRITE UP-SLIP</div>
  <div class="side-item" style="top:543px">
    <svg viewBox="0 0 36 36" fill="none" stroke="var(--brand-blue)" stroke-width="2.5"><rect x="4" y="6" width="24" height="28"/><rect x="11" y="3" width="10" height="6" fill="var(--brand-blue)"/><path d="M9 16h12M9 22h8M9 28h8M20 30l12-14"/></svg>EMPLOYEE PERFORMANCE</div>
</nav>

<main class="form-panel">
  <h1 class="abs form-title">EMPLOYEE DIRECT DEPOSIT ENROLLMENT FORM</h1>
  <p class="abs intro">To enroll in Direct Deposit, simply fill out this form. Attach a voided check for each checking account - not a deposit slip. If depositing to a savings account, ask your bank to give you the Routing/Transit Number for your account It isn't always the same as the number on a savings deposit slip. This will help ensure that you are paid correctly.</p>
  <p class="abs note">Employees must attach a voided check for each of their accounts to help verify their account numbers and bank routing numbers</p>
  <div class="abs attach-box">
    <span class="attach-link">Attach A Voided Check or Bank Deposit Form For The Account</span>
    <span class="btn refresh">REFRESH</span>
  </div>
  <h2 class="abs section-title" style="left:21px;top:268px">ACCOUNT INFORMATION</h2>
  <p class="abs small" style="left:21px;top:294px">The last item must be for the remaining amount owed to you. To distribute to more accounts, please complete another form.</p>
  <p class="abs mid" style="left:21px;top:317px">Make sure to indicate what kind of account, along with enrolling or declining.</p>
  <p class="abs notify" style="left:21px;top:340px">*** NOTIFY PAYROLL IMMEDIATELY IF YOU CLOSE OR CHANGE BANK ACCOUNT</p>
  <div class="abs radio-row" style="left:21px;top:369px">
    <span class="radio"><i></i>New Enrollment</span>
    <span class="radio"><i></i>Change Enrollment</span>
    <span class="radio"><i></i>Cancel Enrollment</span>
  </div>
  <div class="field" style="left:21px;top:403px;width:184px">Bank Name</div>
  <div class="field" style="left:217px;top:403px;width:184px">City</div>
  <div class="field select" style="left:414px;top:403px;width:184px">State</div>
  <div class="field" style="left:21px;top:442px;width:184px">Routing Transit #</div>
  <div class="field" style="left:217px;top:442px;width:381px">Account number</div>
  <div class="abs radio-row" style="left:21px;top:487px">
    <span class="radio"><i></i>Checking</span>
    <span class="radio"><i></i>Saving</span>
  </div>
  <span class="abs" style="left:369px;top:485px;font-size:11px">Amount</span>
  <div class="field" style="left:414px;top:478px;width:184px">100<span style="position:absolute;right:18px">%</span></div>
  <h2 class="abs section-title" style="left:21px;top:527px">IMPORTANT! PLEASE READ AND SIGN BEFORE COMPLETING AND SUBMITTING</h2>
  <p class="abs legal">I hereby authorize SENTINEL WATCH SERVICES to deposit any amounts owed me, as instructed by my employer, by initiating credit entries to my account at the financial institution (hereinafter Bank) indicated on this form. Further, I authorize Bank to accept and to credit any credit entries indicated by SENTINEL WATCH SERVICES to my account.</p>
  <div class="scrollbar"><span></span></div>
</main>

<footer class="site-footer">
  <span class="copyright">© 2016 Company Name&nbsp; All right reserved&nbsp; Term of Use</span>
  <div class="social" aria-label="Social links"><span></span><span></span><span></span><span></span></div>
</footer>
</body>
</html>
```